Brightwell Mechanical - Business Card Design

We would like a dark (likely black) themed business card to be able to hand out to potential clients. We may list our services on the card or keep it clean. Unsure. Logo attached

```html
<!DOCTYPE html>
<html lang="en">
<head>
<meta charset="utf-8">
<title>Brightwell Mechanical – Business Card</title>
<link rel="stylesheet" href="https://fonts.googleapis.com/css2?family=Open+Sans:wght@400;600;700;800&display=swap">
<style>
  :root{
    --page:#2a2522;
    --card:#1b1b1d;
    --blue:#1f6db5;
    --orange:#e35a24;
    --white:#ffffff;
    --muted:#d9d9d9;
  }
  *{box-sizing:border-box;margin:0;padding:0}
  html,body{width:1200px;height:1165px;overflow:hidden;background:var(--page);font-family:"Open Sans",sans-serif}
  .sheet{width:1200px;height:1165px;display:flex;flex-direction:column;align-items:center;justify-content:center;gap:22px}
  .card{position:relative;width:960px;height:549px;background:var(--card);overflow:hidden}

  /* front: contact side */
  .brand-small{position:absolute;left:40px;top:52px;display:flex;align-items:center;gap:14px}
  .brand-small .dot{width:60px;height:60px;border-radius:50%;background:var(--orange)}
  .brand-small .name{color:var(--blue);font-weight:800;font-size:30px;line-height:1.05;text-transform:uppercase;letter-spacing:.5px}
  .brand-small .name small{display:block;font-size:15px;letter-spacing:2px}

  .name-band{position:absolute;left:0;top:248px;width:0;height:0}
  .name-band svg{position:absolute;left:0;top:0}
  .person{position:absolute;left:40px;top:252px;color:var(--white);display:flex;align-items:baseline;gap:12px}
  .person .full{font-weight:700;font-size:36px}
  .person .role{font-size:25px;font-weight:400}

  .contacts{position:absolute;left:40px;top:338px;list-style:none;color:var(--white);font-size:25px;line-height:38px}
  .contacts li{display:flex;align-items:center;gap:10px}
  .contacts svg{width:20px;height:20px;flex:none}
  .contacts .accent{color:var(--orange)}

  .emblem-right{position:absolute;right:-240px;top:66px;width:480px;height:480px;border-radius:50%;border:58px solid var(--orange)}

  /* back: brand side */
  .emblem-left{position:absolute;left:-240px;top:66px;width:480px;height:480px;border-radius:50%;border:58px solid var(--orange)}
  .brand-large{position:absolute;left:285px;top:225px;width:650px;text-align:center;color:var(--blue);font-weight:800;text-transform:uppercase}
  .brand-large .main{display:block;font-size:78px;line-height:1;letter-spacing:1px}
  .brand-large .sub{display:flex;align-items:center;gap:14px;font-size:34px;line-height:1.2;margin-top:6px}
  .brand-large .sub::before,.brand-large .sub::after{content:"";flex:1;height:3px;background:var(--orange)}
  .services{position:absolute;left:285px;top:416px;width:650px;text-align:center;color:var(--muted);font-size:25px;line-height:40px}
  .services span{white-space:nowrap}
  .services span::before{content:"";display:inline-block;width:12px;height:12px;border-radius:50%;background:var(--orange);margin:0 7px 2px 10px}
</style>
</head>
<body>
<main class="sheet">

  <section class="card card-front" aria-label="Card front with contact details">
    <div class="brand-small">
      <span class="dot"></span>
      <span class="name">Brightwell<small>Mechanical Inc</small></span>
    </div>

    <div class="name-band" aria-hidden="true">
      <svg width="600" height="66" viewBox="0 0 600 66">
        <polygon points="0,0 525,0 585,62 0,62" fill="var(--orange)"/>
        <polygon points="0,0 525,0 580,57 0,57" fill="var(--blue)"/>
      </svg>
    </div>
    <div class="person">
      <span class="full">Dana Whitlock</span>
      <span class="role">| President</span>
    </div>

    <ul class="contacts">
      <li><svg viewBox="0 0 20 20"><rect x="5" y="1" width="10" height="18" rx="2" fill="none" stroke="var(--blue)" stroke-width="2"/></svg>555-310-2118</li>
      <li><svg viewBox="0 0 20 20"><path d="M2 8c0-4 16-4 16 0v2h-4V8H6v2H2z M4 11h12v7H4z" fill="var(--blue)"/></svg>555.990.9997</li>
      <li><svg viewBox="0 0 20 20"><rect x="1" y="4" width="18" height="12" fill="var(--blue)"/><path d="M1 4l9 7 9-7" fill="none" stroke="var(--card)" stroke-width="1.6"/></svg>info@brightwellmechanical.com</li>
      <li><svg viewBox="0 0 20 20"><circle cx="10" cy="10" r="9" fill="var(--blue)"/><path d="M1 10h18M10 1c-4 5-4 13 0 18M10 1c4 5 4 13 0 18" fill="none" stroke="var(--card)" stroke-width="1.3"/></svg>www.<span class="accent">brightwellmechanical</span>.com</li>
    </ul>

    <div class="emblem-right" aria-hidden="true"></div>
  </section>

  <section class="card card-back" aria-label="Card back with company name and services">
    <div class="emblem-left" aria-hidden="true"></div>
    <h1 class="brand-large">
      <span class="main">Brightwell</span>
      <span class="sub">Mechanical Inc</span>
    </h1>
    <p class="services">
      <span>Roofing</span> <span>Siding</span> <span>Windows</span> <span>Gutters</span><br>
      <span>Storm Damage</span> <span>Remodeling</span>
    </p>
  </section>

</main>
</body>
</html>
```